Redesign of 3-4 page site for professional services firm

Our site is www.kestrelvaleadvisors.com. We currently have a simple page made with HostPlumo tools. But the tools are not able to generate the look and feel we desire. We need a home page similar to current that tells a little about our company, our experience and our team. We need a second page to show details of current and past transactions we have assisted our clients with. Currently this page reads like a word document but we would like for it to present in a cleaner fashion and liven it up with some images that link to the industry served. For example, a motorcycle outline in a circle for the powersports related transactions. We would like page to introduce each member of "Our Team" and highlight their experience with a photo of each person. If there is no photo available, we would like a placeholder to be their initials in a circle that can be updated later. We would also like a contact us section whether this is a different page or part of the home page.

Target Market(s)

Retirement minded business owners

Industry/Entity Type

Professional Services

Coding

Coded - Design and coding required

Requirements
Must have
• See project description. Must include a page or section for "Current Listings" and "Recently Completed Transactions" (can be same page)

```html
<!DOCTYPE html>
<html lang="en">
<head>
<meta charset="utf-8">
<title>Kestrel Vale Advisors</title>
<link href="https://fonts.googleapis.com/css2?family=Plus+Jakarta+Sans:wght@300;400;500;600;700&display=swap" rel="stylesheet">
<style>
:root{
  --navy:#383a6c;
  --navy-deep:#2f3160;
  --green:#20d07c;
  --lavender:#e7eafb;
  --ink:#1b1b2a;
  --muted:#5a5a6e;
  --line:#cfd0da;
  --white:#ffffff;
}
*{box-sizing:border-box;margin:0;padding:0}
html,body{width:1200px;height:5381px;overflow:hidden}
body{position:relative;background:var(--white);font-family:"Plus Jakarta Sans",sans-serif;color:var(--ink)}
.abs{position:absolute}
.ph{position:absolute;display:block}
.btn{position:absolute;display:flex;align-items:center;justify-content:center;background:var(--green);color:var(--white);font-size:11px;font-weight:600;border-radius:8px;text-decoration:none}
.label{position:absolute;color:var(--green);font-size:17px;font-weight:400}
.title{position:absolute;font-weight:600;color:var(--ink)}
.body-text{position:absolute;font-size:17px;line-height:1.3;color:var(--ink)}

/* hero */
.hero-panel{left:0;top:0;width:592px;height:645px;background:var(--navy)}
.brand{position:absolute;color:var(--white);font-size:24px;font-weight:500;display:flex;align-items:center;gap:10px}
.brand .mark{width:14px;height:14px;border:2px solid var(--white);border-radius:50%}
.nav{left:615px;top:40px;display:flex;gap:20px;font-size:17px;font-weight:600}
.nav a{color:var(--ink);text-decoration:none}
.social-dot{position:absolute;width:14px;height:14px;border-radius:50%;background:var(--white)}
.welcome{left:168px;top:193px;color:var(--white);font-size:25px}
.hero-title{left:168px;top:240px;color:var(--white);font-size:48px;font-weight:600;line-height:1.35;width:520px;z-index:2}

/* about */
.card{position:absolute;background:var(--white);box-shadow:0 4px 16px rgba(0,0,0,.14);border-radius:4px}
.card-title{position:absolute;font-size:17px;font-weight:600}
.card-text{position:absolute;font-size:13px;line-height:1.35;width:245px}

/* listing */
.listing-band{left:0;top:1223px;width:1200px;height:437px;background:var(--navy)}

/* team */
.member{position:absolute;width:246px;height:320px}
.member .photo{position:absolute;left:0;top:0;width:246px;height:275px}
.member .cap{position:absolute;left:10px;top:236px;width:226px;background:var(--white);text-align:center;padding:10px 8px}
.member .side{position:absolute;left:0;top:236px;width:246px;height:42px;background:var(--navy)}
.member h4{font-size:12px;font-weight:600;margin-bottom:4px}
.member p{font-size:7.5px;line-height:1.3;color:var(--muted)}

/* contact */
.contact-band{left:0;top:4740px;width:1200px;height:641px;background:var(--navy)}
.contact-card{left:80px;top:4410px;width:1038px;height:588px;background:var(--white);box-shadow:0 4px 20px rgba(0,0,0,.15);border-radius:4px}
.contact-panel{left:92px;top:4425px;width:423px;height:562px;background:var(--navy);border-radius:6px}
.field-label{position:absolute;font-size:11px;color:var(--muted)}
.field-line{position:absolute;height:1px;background:var(--line)}
.field-value{position:absolute;font-size:11px;color:var(--ink)}

/* footer */
.footer-line{left:75px;top:5068px;width:1047px;height:1px;background:rgba(255,255,255,.35)}
.foot-col{position:absolute;color:var(--white);font-size:12px}
.foot-col h5{font-size:13px;font-weight:500;margin-bottom:18px}
.foot-col a{display:block;color:var(--white);text-decoration:none;margin-bottom:26px;font-size:11px}
.newsletter{left:870px;top:5110px;width:252px;height:130px;background:#4b4d8b;border-radius:6px}
</style>
</head>
<body>

<!-- Hero -->
<div class="abs hero-panel"></div>
<div class="brand" style="left:170px;top:40px"><span class="mark"></span>Kestrel Vale</div>
<nav class="abs nav"><a href="#">Home</a><a href="#">Business Listings</a><a href="#">Our Team</a></nav>
<a class="btn" href="#" style="left:982px;top:35px;width:140px;height:37px">Contact us</a>
<div class="social-dot" style="left:38px;top:195px"></div>
<div class="social-dot" style="left:38px;top:248px"></div>
<div class="social-dot" style="left:38px;top:300px"></div>
<div class="social-dot" style="left:38px;top:353px"></div>
<div class="ph" role="img" aria-label="Business team smiling and shaking hands around a meeting table" style="left:430px;top:92px;width:692px;height:483px;background:linear-gradient(135deg,#6b5a4c,#b59a82 55%,#3d3a3e)"></div>
<div class="abs welcome">Welcome</div>
<h1 class="abs hero-title">Strategically<br>Navigating Business<br>Exits</h1>
<a class="btn" href="#" style="left:165px;top:468px;width:138px;height:37px">Get Strated</a>

<!-- About -->
<div class="label" style="left:0;width:1200px;text-align:center;top:697px">About Us</div>
<h2 class="title" style="left:0;width:1200px;text-align:center;top:728px;font-size:24px">Your Trusted Business Partner</h2>

<div class="card" style="left:75px;top:802px;width:517px;height:338px"></div>
<div class="ph" role="img" aria-label="Businessman in a suit signing documents" style="left:92px;top:830px;width:193px;height:267px;background:linear-gradient(160deg,#3d4148,#9aa0a8 60%,#e2e3e6)"></div>
<div class="card-title" style="left:325px;top:845px">About Our Company</div>
<p class="card-text" style="left:325px;top:878px">Kestrel Vale Advisors facilitates smooth and successful business transactions with full support at every stage. We uphold integrity, transparency, and professionalism to ensure a positive and rewarding experience for all parties involved.</p>
<a class="btn" href="#" style="left:323px;top:1050px;width:160px;height:40px">Learn more</a>

<div class="ph" role="img" aria-label="Financial chart on a dark trading screen" style="left:625px;top:830px;width:193px;height:267px;background:linear-gradient(160deg,#0c1a2e,#2a5d8a 50%,#0f1c2c)"></div>
<div class="card-title" style="left:857px;top:845px">Our Experience</div>
<p class="card-text" style="left:857px;top:878px">With decades of experience, Kestrel Vale Advisors has helped countless clients successfully sell their businesses. Our expert team understands the complexities of business sales — from valuation to closing — and is committed to delivering smooth, results-driven outcomes across diverse industries.</p>
<a class="btn" href="#" style="left:857px;top:1063px;width:160px;height:42px">Learn more</a>

<!-- Current listing -->
<div class="abs listing-band"></div>
<div class="label" style="left:120px;top:1270px">Current Business Listing</div>
<h2 class="title" style="left:120px;top:1303px;font-size:25px;color:var(--white);width:420px;line-height:1.3">Powersports Dealership – North Texas ($1,100,000)</h2>
<p class="body-text" style="left:120px;top:1380px;width:370px;color:var(--white)">Multi-line dealership with high profit and loyal customer base. Managed by experienced staff and has growth potential as the region develops rapidly. Only for serious buyers with proof of funds.</p>
<a class="btn" href="#" style="left:120px;top:1553px;width:160px;height:40px">Show details</a>
<div class="ph" role="img" aria-label="Two professionals shaking hands across a desk" style="left:637px;top:1268px;width:441px;height:454px;background:linear-gradient(150deg,#bfbcb6,#7a6e62 55%,#d8d4ce)"></div>

<!-- Recently sold -->
<div class="label" style="left:653px;top:1836px">Recently Sold Businesses:</div>
<h3 class="title" style="left:653px;top:1874px;font-size:24px">Entertainment &amp; Education</h3>
<p class="body-text" style="left:653px;top:1923px;width:430px">Sports &amp; Entertainment Venue (East Texas) and Flight School (Southern California) offered rare opportunities in dynamic industries with solid assets.</p>
<h3 class="title" style="left:653px;top:2033px;font-size:24px">Professional Services</h3>
<p class="body-text" style="left:653px;top:2082px;width:430px">Bookkeeping &amp; Tax Practice, CPA Firm, and Real Estate Investment Firm in California and Texas delivered high profits through efficient operations and loyal client bases.</p>
<h3 class="title" style="left:653px;top:2193px;font-size:24px">Industrial &amp; Construction</h3>
<p class="body-text" style="left:653px;top:2242px;width:430px">Contractor (Utah) and Dirt Work &amp; Excavating (Northeast Texas) provided essential services with active contracts and strong reputations.</p>
<h3 class="title" style="left:653px;top:2329px;font-size:24px">Powersports Dealerships</h3>
<p class="body-text" style="left:653px;top:2378px;width:430px">Multiple dealerships in North and Northeast Texas were sold, each featuring strong growth, solid teams, and flexible ownership models.</p>
<div class="ph" role="img" aria-label="Business people in suits shaking hands" style="left:122px;top:1927px;width:338px;height:211px;background:linear-gradient(140deg,#1f3566,#5a7bb0 60%,#c9d3e3)"></div>
<div class="ph" role="img" aria-label="Colleagues reviewing a folder in a bright office" style="left:225px;top:2085px;width:340px;height:275px;background:linear-gradient(150deg,#e6e8ec,#9ba6b6 55%,#4b5a74)"></div>

<!-- Team -->
<div class="label" style="left:0;width:1200px;text-align:center;top:2528px">OUR TEAM</div>
<h2 class="title" style="left:0;width:1200px;text-align:center;top:2568px;font-size:24px">The People Behind Your Success</h2>

<div class="member" style="left:75px;top:2665px">
  <div class="photo" role="img" aria-label="Portrait of Marcus Hale" style="background:linear-gradient(180deg,#f2f2f2,#c9ccd3)"></div>
  <div class="side"></div>
  <div class="cap"><h4>Marcus Hale, CPA, JD</h4><p>Marcus is a CPA and JD with expertise in business, finance and tax. He brings strong tax and estate planning skills and business sales know-how to every client he guides.</p></div>
</div>
<div class="member" style="left:345px;top:2665px">
  <div class="photo" role="img" aria-label="Portrait of Dean Corwin" style="background:linear-gradient(180deg,#f2f2f2,#c9ccd3)"></div>
  <div class="side"></div>
  <div class="cap"><h4>Dean Corwin</h4><p>Dean brings over 30 years of experience in finance and insurance, including leadership roles at major firms. His ability to solve complex issues helps clients make informed decisions.</p></div>
</div>
<div class="member" style="left:612px;top:2665px">
  <div class="photo" role="img" aria-label="Portrait of Rory Pell" style="background:linear-gradient(180deg,#f2f2f2,#c9ccd3)"></div>
  <div class="side"></div>
  <div class="cap"><h4>Rory Pell</h4><p>Rory is a sales and marketing veteran in powersports and automotive, founder of a motorsports group, and an expert in profit strategies and customer conversion.</p></div>
</div>
<div class="member" style="left:880px;top:2665px">
  <div class="photo" role="img" aria-label="Portrait of Walter Brisby" style="background:linear-gradient(180deg,#f2f2f2,#c9ccd3)"></div>
  <div class="side"></div>
  <div class="cap"><h4>Walter Brisby</h4><p>Walter is a licensed broker with 40+ years of experience, dedicated to helping clients sell their businesses through precise and strategic negotiation.</p></div>
</div>

<!-- Transactions in progress -->
<div class="abs" style="left:0;top:3180px;width:1200px;height:460px;background:var(--lavender)"></div>
<div class="ph" role="img" aria-label="Handshake over a desk with phones and notebook" style="left:75px;top:3100px;width:523px;height:540px;background:linear-gradient(150deg,#d9cfc4,#a89684 55%,#5c4c40)"></div>
<div class="label" style="left:697px;top:3222px">Current Transactions in Progress</div>
<h2 class="title" style="left:697px;top:3255px;font-size:25px;width:400px;line-height:1.3">Guiding Our Clients Toward Successful Closures</h2>
<p class="body-text" style="left:697px;top:3342px;width:425px">We are actively assisting clients across various industries in navigating high-value and complex transactions. Below is a list of current engagements we are managing—from powersports to real estate—each handled with precision, professionalism, and dedication. Follow our progress and see how we're delivering real results every step of the way.</p>
<a class="btn" href="#" style="left:697px;top:3573px;width:160px;height:40px">Get Strated</a>

<!-- Recently closed -->
<div class="abs" style="left:0;top:3735px;width:1200px;height:445px;background:var(--lavender)"></div>
<div class="label" style="left:77px;top:3740px">Recently Closed Transactions</div>
<h2 class="title" style="left:77px;top:3773px;font-size:25px;width:420px;line-height:1.3">A Track Record of Successful Outcomes</h2>
<p class="body-text" style="left:77px;top:3860px;width:425px">We are proud to be a trusted partner in completing significant deals for our clients. Every closed transaction reflects our team's experience, strategic insight, and full commitment. Explore some of our recent successes, complete with project highlights, transaction values, and the industries we serve.</p>
<a class="btn" href="#" style="left:75px;top:4074px;width:162px;height:42px">Get Strated</a>
<div class="ph" role="img" aria-label="Handshake over a desk with phones and notebook" style="left:600px;top:3735px;width:522px;height:537px;background:linear-gradient(150deg,#d9cfc4,#a89684 55%,#5c4c40)"></div>

<!-- Contact -->
<div class="abs contact-band"></div>
<div class="abs contact-card"></div>
<div class="abs contact-panel"></div>
<div class="abs" style="left:124px;top:4458px;color:var(--white);font-size:22px;font-weight:600">Contact Information</div>
<div class="abs" style="left:124px;top:4502px;color:#c9cae0;font-size:13px">Say something to start a live chat!</div>
<svg class="abs" style="left:124px;top:4620px" width="18" height="18" viewBox="0 0 24 24"><path d="M6.6 10.8a15 15 0 0 0 6.6 6.6l2.2-2.2a1 1 0 0 1 1-.25 11.4 11.4 0 0 0 3.6.6 1 1 0 0 1 1 1V20a1 1 0 0 1-1 1A17 17 0 0 1 3 4a1 1 0 0 1 1-1h3.5a1 1 0 0 1 1 1c0 1.25.2 2.45.6 3.6a1 1 0 0 1-.25 1z" fill="#fff"/></svg>
<div class="abs" style="left:166px;top:4622px;color:var(--white);font-size:13px">+1-555-204-7718</div>
<svg class="abs" style="left:124px;top:4687px" width="18" height="14" viewBox="0 0 24 18"><rect x="0" y="0" width="24" height="18" rx="2" fill="#fff"/><path d="M1 2l11 8 11-8" stroke="#383a6c" stroke-width="2" fill="none"/></svg>
<div class="abs" style="left:166px;top:4686px;color:var(--white);font-size:13px">hello@kestrelvaleadvisors.com</div>
<div class="social-dot" style="left:124px;top:4930px;width:22px;height:22px"></div>
<div class="social-dot" style="left:171px;top:4930px;width:22px;height:22px"></div>
<div class="social-dot" style="left:218px;top:4930px;width:22px;height:22px"></div>

<div class="field-label" style="left:557px;top:4473px">First Name</div>
<div class="field-value" style="left:557px;top:4498px">|</div>
<div class="field-line" style="left:557px;top:4525px;width:243px"></div>
<div class="field-label" style="left:832px;top:4473px;color:var(--ink)">Last Name</div>
<div class="field-value" style="left:832px;top:4498px;color:var(--muted)">Doe</div>
<div class="field-line" style="left:832px;top:4525px;width:243px"></div>
<div class="field-label" style="left:557px;top:4558px">Email</div>
<div class="field-line" style="left:557px;top:4610px;width:243px"></div>
<div class="field-label" style="left:832px;top:4558px;color:var(--ink)">Phone Number</div>
<div class="field-value" style="left:832px;top:4580px">+1-555-204-7718</div>
<div class="field-line" style="left:832px;top:4610px;width:243px;background:var(--ink)"></div>
<div class="field-label" style="left:557px;top:4730px">Message</div>
<div class="field-value" style="left:557px;top:4752px;color:var(--muted)">Write your message..</div>
<div class="field-line" style="left:557px;top:4783px;width:518px;background:var(--muted)"></div>
<a class="btn" href="#" style="left:888px;top:4820px;width:185px;height:45px;border-radius:24px;font-size:13px">Send Message</a>

<!-- Footer -->
<div class="abs footer-line"></div>
<div class="brand" style="left:90px;top:5188px;font-size:30px"><span class="mark" style="width:18px;height:18px"></span>Kestrel Vale</div>
<div class="foot-col" style="left:388px;top:5125px"><h5>Company</h5><a href="#" style="font-weight:600">About Us</a><a href="#">Contact</a></div>
<div class="foot-col" style="left:515px;top:5125px"><h5>Legal</h5><a href="#">Privacy Policy</a><a href="#">Terms &amp; Services</a><a href="#">Terms of Use</a><a href="#">Refund Policy</a></div>
<div class="foot-col" style="left:678px;top:5125px"><h5>Quick Links</h5><a href="#">Home</a><a href="#">Business Listings</a></div>
<div class="abs newsletter"></div>
<div class="abs" style="left:880px;top:5125px;color:var(--white);font-size:14px;font-weight:600">Join Our Newsletter</div>
<div class="abs" style="left:880px;top:5158px;width:142px;height:30px;background:var(--white);font-size:8px;color:var(--muted);padding:10px 8px">Your email address</div>
<div class="abs" style="left:1022px;top:5158px;width:90px;height:30px;background:#6a3fd0;color:var(--white);font-size:9px;display:flex;align-items:center;justify-content:center">Subscribe</div>
<div class="abs" style="left:880px;top:5200px;width:220px;color:#c9cae0;font-size:8px;line-height:1.35">* We will send you weekly updates for your better deal management.</div>
<div class="abs" style="left:0;width:1200px;text-align:center;top:5347px;color:var(--white);font-size:11px">Kestrel Vale - All Rights Reserved. Copyright © 2025</div>

</body>
</html>
```